Create Bourbon label for Craft Distillery located in the Foothills of NC.

Need to create a label for a craft bourbon. The brand name is Brookfen. Looking for a traditional/vintage bottle label. I have created a concept and would like an expansion of the concept idea (open to artwork outside of concept art as well). I have included the bottle being used. Label area approx 4.25H x 3.5W. With the Brookfen brand name, would like to incorporate trees (native to NC and Appalachia), mountains (mt pano of area included), and sawblade. However, I do not want the sawblade to be the focal point of the design. The word Bourbon, proof, abv, and 750 ml will need to be horizontal. Brookfen and Made in NC can be angled in the design.

Requirements
Must have
• Front Label will need to contain the followingBrand Name = SawmillsBourbon750 ml100 Proof50% ABVAged 3 years

```html
<!DOCTYPE html>
<html lang="en">
<head>
<meta charset="utf-8">
<title>Brookfen Bourbon Label</title>
<link rel="stylesheet" href="https://fonts.googleapis.com/css2?family=Rye&family=Stardos+Stencil:wght@700&family=Roboto+Slab:wght@700&family=Roboto+Condensed:wght@700&display=swap">
<style>
  :root {
    --paper-light: #f3e0bb;
    --paper-dark: #e2c48f;
    --ink-brown: #5a3214;
    --rule-brown: #7a4f2a;
    --hill-tan: #d8ab6e;
    --hill-deep: #b98447;
    --cream: #f6e0b6;
    --canvas-bg: #ffffff;
  }
  * { margin: 0; padding: 0; box-sizing: border-box; }
  html, body {
    width: 1183px; height: 1200px; overflow: hidden;
    background: var(--canvas-bg);
  }
  .label {
    position: absolute; left: 111px; top: 17px;
    width: 960px; height: 1166px;
    background: radial-gradient(ellipse at 55% 35%, var(--paper-light) 0%, var(--paper-dark) 100%);
    color: var(--ink-brown);
  }
  .rule-top {
    position: absolute; left: 153px; top: 47px; width: 659px; height: 2px;
    background: var(--rule-brown);
  }
  .rule-side {
    position: absolute; top: 166px; width: 2px; height: 839px;
    background: var(--rule-brown);
  }
  .rule-side.left { left: 24px; }
  .rule-side.right { left: 934px; }
  .made-in {
    position: absolute; left: 0; width: 100%; top: 178px;
    text-align: center;
    font: 700 44px "Roboto Slab", serif;
    letter-spacing: 1px;
  }
  .brand {
    position: absolute; left: 0; width: 100%; top: 236px;
    text-align: center;
    font: 400 128px "Rye", serif;
    line-height: 1;
    color: var(--ink-brown);
  }
  .scene {
    position: absolute; left: 54px; top: 488px; width: 853px; height: 581px;
  }
  .scene-art {
    position: absolute; left: 0; top: 0; width: 100%; height: 320px;
    background: linear-gradient(180deg, rgba(216,171,110,0) 0%, var(--hill-tan) 30%, var(--hill-deep) 75%, var(--ink-brown) 100%);
  }
  .scene-panel {
    position: absolute; left: 0; top: 320px; width: 100%; height: 261px;
    background: var(--ink-brown);
    color: var(--cream);
  }
  .spirit {
    position: absolute; left: 0; width: 100%; top: 42px;
    text-align: center;
    font: 700 96px "Stardos Stencil", serif;
    line-height: 1;
    letter-spacing: 2px;
  }
  .age {
    position: absolute; left: 0; width: 100%; top: 150px;
    display: flex; justify-content: center; align-items: center; gap: 14px;
    font: 700 28px "Roboto Condensed", sans-serif;
  }
  .age .num { font-size: 34px; }
  .age-dash { width: 76px; height: 7px; border-top: 2px solid var(--cream); border-bottom: 2px solid var(--cream); opacity: .8; }
  .strength {
    position: absolute; top: 218px;
    font: 700 27px "Roboto Condensed", sans-serif;
  }
  .strength.proof { left: 21px; }
  .strength.abv { right: 22px; }
  .rule-bottom {
    position: absolute; top: 1118px; height: 2px; width: 130px;
    background: var(--rule-brown);
  }
  .rule-bottom.left { left: 153px; }
  .rule-bottom.right { left: 682px; }
  .diamond {
    position: absolute; top: 1111px; width: 14px; height: 14px;
    background: var(--rule-brown); transform: rotate(45deg);
  }
  .diamond.left { left: 300px; }
  .diamond.right { left: 646px; }
  .volume {
    position: absolute; left: 329px; top: 1095px; width: 301px; height: 47px;
    border-radius: 24px;
    background: #6f4520;
    color: var(--cream);
    text-align: center;
    font: 700 32px "Roboto Slab", serif;
    line-height: 47px;
  }
</style>
</head>
<body>
  <div class="label">
    <div class="rule-top"></div>
    <div class="rule-side left"></div>
    <div class="rule-side right"></div>

    <div class="made-in">MADE IN NC</div>
    <div class="brand">BROOKFEN</div>

    <div class="scene">
      <div class="scene-art" role="img" aria-label="Mountain peak silhouette behind a line of pine and hardwood trees"></div>
      <div class="scene-panel">
        <div class="spirit">BOURBON</div>
        <div class="age"><span class="age-dash"></span><span>AGED <span class="num">3</span> YEARS</span><span class="age-dash"></span></div>
        <div class="strength proof">100 Proof</div>
        <div class="strength abv">50% ABV</div>
      </div>
    </div>

    <div class="rule-bottom left"></div>
    <div class="diamond left"></div>
    <div class="volume">750ml</div>
    <div class="diamond right"></div>
    <div class="rule-bottom right"></div>
  </div>
</body>
</html>
```